UI design for Fast Food Restaurant Self-Order App

Background:
App purpose: for fast food restaurant customers to self order food/drink by choosing item image, and make payment by tapping the credit card on the card terminal.
Reference: https://www.brivolkiosks.example/product-overview/self-order-kiosks/
Attachment:
Wireframes. (wire frames provide general idea and the information to display, they are not a strict guideline for layout design.)
Tarrowby's Self ordering app.
Intro:
We have built a (for restaurant and cafe) Self Ordering and Payment app, similar to Tarrowby's self ordering software in most of their new restaurants. Our app will be placed in a Quorvane Deskline 10 OS touch screen Kiosk(screen size 4:3 or Portrait 16:9) within the restaurant/cafe premise.
Pages to be designed:
Page 1. Food Browsing Page. displays all food images(to be provided by cafes) by categories, and displays the Cart. This page will lead to Page 2 or Page 3.
'Cart' section should include:
'cart items/selected items', its quantity and price. like Tarrowbys' app.
When click on a Cart Item, we need to allow to change quantity or 'change Choice'. The UI handling these change requests with ease will be one deciding factor for us to choose your design.
Fact: up to 10 food categories, and 10 - 25 food items under each categories.
When click on one item image, it goes to Page 2.
Page 2. Item Detail/Description Page. Shows description of the food, and its available Choice(other food items or Special Request, up to 12) will also be displayed. 'Add item to cart' action(Button Name: ADD) will happen here and go back to Browsing Page 1.
e.g. Item 'Fried Rice' Page. the Choice could be 'Add Egg', 'Add Meat', 'No Chilli' etc.
Page 3. Order Review Page. No edit features allowed on this page, only two buttons: 'No' to go back to Browsing Page, or 'Yes' to proceed to Payment Page 4. Check Tarrowby's screen.
Page 4. Payment Page - Prompt user to Insert or Tap credit card on the credit card terminal. (Exact wording: PLEASE FOLLOW INSTRUCTIONS DISPLAYED ON CREDIT CARD TERMINAL BELOW)
Page 5. Payment status. Successful / Failed.
Our considerations to pick the winner:
1. In terms of design for this task, we look out for page layout, effects, fonts, button style and overall colour scheme. the design should present itself in a clean and modern look, with minimum clicking or scrolling. The app aims to help customers choose and pay for their items quickly.
2.we need to handle both 4:3(as shown in wire frames) and 16:9 screens(like Tarrowby's). there will be a lot more vertical space to utilise when it is in 16:9, resulting less scrolling than 4:3. tell us what you think.
All questions are welcome.
Winner has opportunity to work on a few more app UI. Cheers!
Industry/Entity Type
Fast Food Restaurant
Requirements
Must have
- Button colour differentiation - helps people know what to click next.
- best use of screen space. minimum click and scrolls.
Nice to have
- any personal touch.
Should not have
- unrelated design pattern, e.g. a cute animal or flower pattern in the layout.

```html
<!DOCTYPE html>
<html lang="en">
<head>
<meta charset="UTF-8">
<title>Brivolane – Self-Order Kiosk</title>
<link href="https://fonts.googleapis.com/css2?family=Catamaran:wght@400;500;600;700;800&display=swap" rel="stylesheet">
<style>
  :root{
    --page-bg:#f1f6fd;
    --page-shape:#dce9f8;
    --page-shape-deep:#c4dbf4;
    --panel:#ffffff;
    --grid-bg:#f7f9fc;
    --ink:#2b2f36;
    --ink-soft:#4a4f58;
    --muted:#a2a7ae;
    --line:#e6e9ee;
    --brand:#0d3ca6;
    --brand-light:#2356c4;
    --active-row:#e9f0fb;
    --step-btn:#c8d5e3;
    --danger:#ff4b4b;
    --search:#eef1f4;
  }
  *{box-sizing:border-box;margin:0;padding:0}
  html,body{width:1200px;height:900px;overflow:hidden}
  body{background:var(--page-bg);font-family:"Catamaran",sans-serif;color:var(--ink);position:relative}
  .backdrop{position:absolute;inset:0}
  .kiosk{position:absolute;left:88px;top:130px;width:1024px;height:640px;background:var(--panel);
    box-shadow:0 10px 30px rgba(40,80,140,.12);display:flex}

  /* left: browsing area */
  .browse{width:640px;display:flex;flex-direction:column}
  .topbar{height:54px;display:flex;align-items:center;position:relative;background:var(--panel);
    box-shadow:0 2px 6px rgba(0,0,0,.03);z-index:1}
  .hamburger{position:absolute;left:21px;top:20px;width:22px;height:16px}
  .brand{position:absolute;left:62px;top:16px;color:var(--ink);font-weight:600;font-size:22px;line-height:1}
  .search{position:absolute;left:230px;top:14px;width:389px;height:28px;background:var(--search);
    border-radius:3px;display:flex;align-items:center;padding:0 12px 0 18px;font-size:12px;color:var(--muted)}
  .search svg{margin-left:auto}
  .browse-body{flex:1;display:flex}
  .sidebar{width:208px;background:var(--panel);padding-top:26px}
  .sidebar h2{font-size:14px;font-weight:800;color:var(--brand);letter-spacing:.6px;padding-left:21px;margin-bottom:17px}
  .cat{height:41px;display:flex;align-items:center;padding-left:21px;font-size:13px;color:var(--ink-soft);font-weight:500}
  .cat svg{width:20px;height:20px;margin-right:12px;flex:none}
  .cat.is-active{background:var(--active-row);color:var(--brand-light)}
  .menu-grid{flex:1;background:var(--grid-bg);padding:21px 0 0 14px;display:grid;
    grid-template-columns:repeat(3,122px);grid-auto-rows:185px;column-gap:20px}
  .dish{text-align:center}
  .dish-photo{width:122px;height:122px;border-radius:3px}
  .dish-name{font-size:12.5px;font-weight:500;color:var(--ink);margin-top:8px;line-height:1.2;white-space:nowrap}
  .dish-price{font-size:12px;color:var(--muted);margin-top:2px}
  .warm{background:radial-gradient(circle at 50% 50%,#e0733a 0,#d99a5a 26%,#f3f1ee 44%,#ffffff 60%)}
  .red{background:radial-gradient(circle at 50% 50%,#d9402a 0,#e2793f 26%,#f2f0ee 44%,#ffffff 60%)}
  .brown{background:radial-gradient(circle at 50% 50%,#b06a34 0,#c9905a 26%,#eeece9 44%,#fbfbfb 60%)}
  .grey{background:radial-gradient(circle at 50% 50%,#d8b98a 0,#c9b59a 24%,#e6e7e9 44%,#f0f1f3 60%)}

  /* right: cart */
  .cart{width:384px;padding:0 22px;position:relative;border-left:1px solid #f0f2f5}
  .cart-head{height:54px;display:flex;align-items:center;border-bottom:1px solid var(--line)}
  .cart-head h1{flex:1;text-align:center;font-size:20px;font-weight:500}
  .order-meta{height:45px;display:flex;align-items:center;border-bottom:1px solid var(--line);font-size:14px}
  .order-id{color:var(--brand);font-weight:600}
  .order-time{margin-left:auto;color:var(--muted)}
  .cart-item{height:83px;border-bottom:1px solid var(--line);padding-top:9px;position:relative}
  .item-name{font-size:15px;font-weight:500;line-height:1.2}
  .item-price{font-size:14px;color:var(--muted);margin-top:3px}
  .item-note{font-size:11.5px;color:var(--muted);margin-top:2px;display:flex;align-items:center}
  .item-note svg{margin-right:7px}
  .stepper{position:absolute;right:8px;top:32px;display:flex;gap:10px}
  .step{width:24px;height:24px;background:var(--step-btn);border-radius:2px;display:flex;align-items:center;justify-content:center}
  .qty{width:24px;height:24px;border:1px solid #b9bfc6;border-radius:2px;font-size:13px;display:flex;align-items:center;justify-content:center;padding-top:2px}
  .scroll-track{position:absolute;right:10px;top:120px;width:1px;height:315px;background:var(--line)}
  .scroll-thumb{position:absolute;right:9px;top:245px;width:3px;height:63px;background:var(--brand)}
  .summary{margin-top:16px}
  .sum-row{display:flex;justify-content:space-between;font-size:15px;font-weight:500;height:28px;align-items:center}
  .sum-total{font-size:19px;font-weight:700;margin-top:11px}
  .actions{display:flex;gap:20px;margin-top:13px}
  .btn{flex:1;height:44px;display:flex;align-items:center;justify-content:center;color:#fff;font-weight:700;
    font-size:14px;letter-spacing:.4px;border-radius:2px;padding-top:2px}
  .btn-cancel{background:var(--danger)}
  .btn-pay{background:var(--brand)}
</style>
</head>
<body>
<svg class="backdrop" width="1200" height="900" viewBox="0 0 1200 900" aria-hidden="true">
  <path d="M380 0 Q470 90 520 130 L1112 130 L1112 0 Z" fill="var(--page-shape)"/>
  <path d="M380 0 Q440 70 520 130 L600 130 Q520 60 470 0 Z" fill="var(--page-shape-deep)" opacity=".6"/>
  <path d="M0 0 L300 0 Q160 160 88 245 Q40 240 0 235 Z" fill="#e6effa"/>
  <path d="M1112 700 Q1170 760 1200 800 L1200 900 L1112 900 Z" fill="#e6effa"/>
</svg>

<main class="kiosk">
  <section class="browse">
    <header class="topbar">
      <svg class="hamburger" viewBox="0 0 22 16"><g stroke="#2b2f36" stroke-width="2"><line x1="0" y1="1" x2="22" y2="1"/><line x1="0" y1="8" x2="22" y2="8"/><line x1="0" y1="15" x2="22" y2="15"/></g></svg>
      <div class="brand">Brivolane</div>
      <div class="search">Search Menu
        <svg width="15" height="15" viewBox="0 0 15 15"><circle cx="6.5" cy="6.5" r="5" fill="none" stroke="#8a9099" stroke-width="1.4"/><line x1="10.2" y1="10.2" x2="14" y2="14" stroke="#8a9099" stroke-width="1.4"/></svg>
      </div>
    </header>
    <div class="browse-body">
      <nav class="sidebar">
        <h2>MENU BOARD</h2>
        <div class="cat"><svg viewBox="0 0 20 20" fill="none" stroke="#555" stroke-width="1.2"><rect x="3" y="6" width="14" height="12" rx="1"/><path d="M6 6V3h8v3"/><line x1="3" y1="10" x2="17" y2="10"/></svg>Toast</div>
        <div class="cat"><svg viewBox="0 0 20 20" fill="none" stroke="#555" stroke-width="1.2"><path d="M4 10h12l-2 8H6z"/><path d="M4 10a6 5 0 0 1 12 0"/></svg>Cakes</div>
        <div class="cat is-active"><svg viewBox="0 0 20 20" fill="none" stroke="#2356c4" stroke-width="1.4"><path d="M2 10h16a8 7 0 0 1-16 0z"/><line x1="6" y1="2" x2="12" y2="10"/><line x1="9" y1="2" x2="14" y2="10"/></svg>Noodle</div>
        <div class="cat"><svg viewBox="0 0 20 20" fill="none" stroke="#555" stroke-width="1.2"><path d="M2 10h16a8 7 0 0 1-16 0z"/><path d="M5 10a5 4 0 0 1 10 0"/><line x1="12" y1="3" x2="17" y2="7"/></svg>Fried Rice</div>
        <div class="cat"><svg viewBox="0 0 20 20" fill="none" stroke="#555" stroke-width="1.2"><ellipse cx="10" cy="10" rx="8" ry="6" transform="rotate(-35 10 10)"/><path d="M6 13l8-7"/></svg>Beef Steak</div>
        <div class="cat"><svg viewBox="0 0 20 20" fill="none" stroke="#555" stroke-width="1.2"><path d="M4 16c-2-4 1-8 6-8l4-4 2 2-4 4c0 5-4 8-8 6z"/><line x1="2" y1="18" x2="5" y2="15"/></svg>Crispy Chicken</div>
        <div class="cat"><svg viewBox="0 0 20 20" fill="none" stroke="#555" stroke-width="1.2"><circle cx="10" cy="10" r="7.5"/><line x1="10" y1="6" x2="10" y2="14"/><line x1="6" y1="10" x2="14" y2="10"/></svg>Add Ons</div>
      </nav>
      <div class="menu-grid">
        <div class="dish"><div class="dish-photo warm" role="img" aria-label="Photo of Bakmi Special noodle bowl with chopsticks"></div><div class="dish-name">Bakmi Special</div><div class="dish-price">$ 65</div></div>
        <div class="dish"><div class="dish-photo red" role="img" aria-label="Photo of Bakmi Komplit Special on a white plate"></div><div class="dish-name">Bakmi Komplit Special</div><div class="dish-price">$ 110</div></div>
        <div class="dish"><div class="dish-photo brown" role="img" aria-label="Photo of Bakmi Ayam Teriyaki on a white plate"></div><div class="dish-name">Bakmi Ayam Teriyaki</div><div class="dish-price">$ 78</div></div>
        <div class="dish"><div class="dish-photo red" role="img" aria-label="Photo of Bakmi Kuah Sapi on a plate"></div><div class="dish-name">Bakmi Kuah Sapi</div><div class="dish-price">$ 45</div></div>
        <div class="dish"><div class="dish-photo brown" role="img" aria-label="Photo of Bakmi Sapi Hitam on a plate"></div><div class="dish-name">Bakmi Sapi Hitam</div><div class="dish-price">$ 52</div></div>
        <div class="dish"><div class="dish-photo grey" role="img" aria-label="Photo of Bakmi Seafood Pedas on a plate"></div><div class="dish-name">Bakmi Seafood Pedas</div><div class="dish-price">$ 52</div></div>
        <div class="dish"><div class="dish-photo red" role="img" aria-label="Photo of Bakmi Goreng Ayam on a plate"></div><div class="dish-name">Bakmi Goreng Ayam</div><div class="dish-price">$ 38</div></div>
        <div class="dish"><div class="dish-photo brown" role="img" aria-label="Photo of Bakmi Goreng Seafood on a plate"></div><div class="dish-name">Bakmi Goreng Seafood</div><div class="dish-price">$ 60</div></div>
        <div class="dish"><div class="dish-photo warm" role="img" aria-label="Photo of Bakmi Capcay on a blue plate"></div><div class="dish-name">Bakmi Capcay</div><div class="dish-price">$ 78</div></div>
      </div>
    </div>
  </section>

  <aside class="cart">
    <div class="cart-head">
      <svg width="20" height="16" viewBox="0 0 20 16"><g fill="#2b2f36"><circle cx="2" cy="2" r="1.6"/><circle cx="2" cy="8" r="1.6"/><circle cx="2" cy="14" r="1.6"/><rect x="6" y="1" width="14" height="2"/><rect x="6" y="7" width="14" height="2"/><rect x="6" y="13" width="14" height="2"/></g></svg>
      <h1>Cart (4)</h1>
      <svg width="18" height="18" viewBox="0 0 18 18"><g stroke="#2b2f36" stroke-width="2"><line x1="9" y1="0" x2="9" y2="18"/><line x1="0" y1="9" x2="18" y2="9"/></g></svg>
    </div>
    <div class="order-meta"><span class="order-id">Oder List#1</span><span class="order-time">Delia, 8 Feb 2018 | 17:51:27</span></div>

    <div class="cart-item">
      <div class="item-name">Bakmi Komplit Special</div><div class="item-price">$ 220</div>
      <div class="item-note"><svg width="13" height="13" viewBox="0 0 13 13" fill="none" stroke="#a2a7ae" stroke-width="1"><rect x=".5" y="2.5" width="10" height="10"/><path d="M5 8l7-7"/></svg>Notes</div>
      <div class="stepper"><span class="step"><svg width="12" height="2"><rect width="12" height="2" fill="#fff"/></svg></span><span class="qty">2</span><span class="step"><svg width="12" height="12"><rect y="5" width="12" height="2" fill="#fff"/><rect x="5" width="2" height="12" fill="#fff"/></svg></span></div>
    </div>
    <div class="cart-item">
      <div class="item-name">Bakmi Ayam Teriyaki</div><div class="item-price">$ 95</div>
      <div class="item-note"><svg width="13" height="13" viewBox="0 0 13 13" fill="none" stroke="#a2a7ae" stroke-width="1"><rect x=".5" y="2.5" width="10" height="10"/><path d="M5 8l7-7"/></svg>Do not have too much sauce</div>
      <div class="stepper"><span class="step"><svg width="12" height="2"><rect width="12" height="2" fill="#fff"/></svg></span><span class="qty">1</span><span class="step"><svg width="12" height="12"><rect y="5" width="12" height="2" fill="#fff"/><rect x="5" width="2" height="12" fill="#fff"/></svg></span></div>
    </div>
    <div class="cart-item">
      <div class="item-name">French Fries Original</div><div class="item-price">$ 36</div>
      <div class="item-note"><svg width="13" height="13" viewBox="0 0 13 13" fill="none" stroke="#a2a7ae" stroke-width="1"><rect x=".5" y="2.5" width="10" height="10"/><path d="M5 8l7-7"/></svg>Plus the cheese seasoning</div>
      <div class="stepper"><span class="step"><svg width="12" height="2"><rect width="12" height="2" fill="#fff"/></svg></span><span class="qty">3</span><span class="step"><svg width="12" height="12"><rect y="5" width="12" height="2" fill="#fff"/><rect x="5" width="2" height="12" fill="#fff"/></svg></span></div>
    </div>
    <div class="cart-item">
      <div class="item-name">Hot Coffee Large</div><div class="item-price">$ 80</div>
      <div class="item-note"><svg width="13" height="13" viewBox="0 0 13 13" fill="none" stroke="#a2a7ae" stroke-width="1"><rect x=".5" y="2.5" width="10" height="10"/><path d="M5 8l7-7"/></svg>Notes</div>
      <div class="stepper"><span class="step"><svg width="12" height="2"><rect width="12" height="2" fill="#fff"/></svg></span><span class="qty">2</span><span class="step"><svg width="12" height="12"><rect y="5" width="12" height="2" fill="#fff"/><rect x="5" width="2" height="12" fill="#fff"/></svg></span></div>
    </div>
    <span class="scroll-track"></span><span class="scroll-thumb"></span>

    <div class="summary">
      <div class="sum-row"><span>Sub Total</span><span>$ 431</span></div>
      <div class="sum-row"><span>Discount (0%)</span><span>$ 0</span></div>
      <div class="sum-row"><span>10% Tax</span><span>$ 43</span></div>
      <div class="sum-row sum-total"><span>Total</span><span>$ 474</span></div>
    </div>
    <div class="actions">
      <span class="btn btn-cancel">CANCEL</span>
      <span class="btn btn-pay">PAY</span>
    </div>
  </aside>
</main>
</body>
</html>
```